innovative investment real estate sales firm

We are a uniquely collabrative firm that seeks to bring a conultative approach to uncovering hidden opportunities for our clients, our website needs to convey our client focused approach. Our firm specializes in the sale of apartment properties in Southern California. We have a team of researchers, transaction coordinators and marketing personal to support our geographically specialized advisers. We need a website that introduces clients to our unique way of better helping them achieve their investment goals.

Target Market(s)

High net worth individuals and families

Industry/Entity Type

Real Estate Agent

Font styles to use
Other font styles liked:
• please use font provided

Requirements
Must have
• Stories of our recent projects
• Features on our people
• email capture for viewing inventory
• content that showcases our unique consultative approach that uncovers unrealized opportunities

```html
<!DOCTYPE html>
<html lang="en">
<head>
<meta charset="utf-8">
<title>Meridian Advisers — MultiFamily Properties</title>
<link rel="stylesheet" href="https://fonts.googleapis.com/css2?family=Hind:wght@400;500;600&family=Montserrat:wght@500;600;700&display=swap">
<style>
:root{
  --teal:#0ea1b8;
  --teal-dark:#0a8aa0;
  --slate:#4a5560;
  --ink:#3d4650;
  --muted:#7d858c;
  --topbar:#e2e3e3;
  --navy:#1d4f7a;
  --navy-card:#2a69a6;
  --lime:#8cc63f;
  --white:#ffffff;
}
*{margin:0;padding:0;box-sizing:border-box}
html,body{width:1200px;height:2884px;overflow:hidden;background:var(--white)}
body{position:relative;font-family:"Hind",Arial,sans-serif;color:var(--ink)}
.abs{position:absolute}
.heading{font-family:"Montserrat",Arial,sans-serif;font-weight:700}

/* top bar & header */
.topbar{left:0;top:0;width:1200px;height:20px;background:var(--topbar);font-size:11px;color:#9a9fa3;display:flex;justify-content:flex-end;align-items:center;padding-right:158px;gap:14px}
.header{left:0;top:20px;width:1200px;height:77px;background:var(--white)}
.brand{left:163px;top:47px;display:flex;align-items:center;gap:10px}
.brand-mark{width:22px;height:22px;background:var(--teal)}
.brand-name{font-family:"Montserrat",sans-serif;font-weight:600;font-size:16px;line-height:22px;color:var(--teal);letter-spacing:1px;text-transform:uppercase}
.nav{left:480px;top:53px;display:flex;gap:13px;font-family:"Montserrat",sans-serif;font-weight:600;font-size:11px;letter-spacing:.8px;color:var(--ink);text-transform:uppercase;white-space:nowrap}
.nav .active{color:var(--teal)}

.hero{left:0;top:97px;width:1200px;height:426px;background:linear-gradient(180deg,#8fb3d3 0%,#c9d6df 30%,#8a6a4e 55%,#4f6a3a 78%,#6f9a3d 100%)}

/* services */
.service{top:585px;width:200px;text-align:center}
.service-icon{width:70px;height:70px;border-radius:50%;background:var(--slate);margin:0 auto;display:flex;align-items:center;justify-content:center}
.service-icon.is-active{background:var(--teal)}
.service-title{margin-top:16px;font-family:"Montserrat",sans-serif;font-weight:600;font-size:12.5px;letter-spacing:3px;line-height:23px;color:var(--ink);text-transform:uppercase}
.service-text{margin-top:10px;font-size:13px;line-height:23px;color:var(--muted)}

/* about */
.about-label{left:184px;top:884px;font-family:"Montserrat",sans-serif;font-weight:700;font-size:14px;letter-spacing:2px;color:var(--teal)}
.about-title{left:184px;top:899px;font-size:27px;color:var(--slate);letter-spacing:.5px;border-bottom:3px solid var(--teal);padding-bottom:2px;white-space:nowrap}
.about-text{left:184px;top:950px;width:410px;font-size:14px;line-height:24px;color:var(--muted)}
.about-photo{left:615px;top:817px;width:585px;height:243px;background:linear-gradient(120deg,#9ab6cf 0%,#dfe6ee 45%,#c79b55 75%,#7c8a9a 100%)}

/* section headings */
.section-title{left:0;width:1200px;text-align:center}
.section-title span{font-size:24px;color:var(--slate);letter-spacing:1px;border-bottom:3px solid var(--teal);padding-bottom:2px}

/* projects */
.project-photo{background:linear-gradient(180deg,#a8c6e0 0%,#c8b49a 45%,#6e8a4d 80%,#8db05a 100%)}
.project-label{display:flex;align-items:center;justify-content:center;background:var(--slate);color:var(--white);font-family:"Montserrat",sans-serif;font-weight:700;font-size:17px}
.project-label.is-featured{background:var(--teal)}

/* news */
.news{top:2090px;width:260px;display:flex;gap:26px}
.news-date{width:40px;height:78px;background:var(--teal);color:var(--white);text-align:center;padding-top:6px;flex:none}
.news-date .day{font-family:"Montserrat",sans-serif;font-weight:700;font-size:26px;line-height:28px;margin-top:6px}
.news-date .month{font-size:12px;line-height:14px}
.news-title{font-family:"Montserrat",sans-serif;font-weight:700;font-size:15px;color:var(--slate);border-bottom:2px solid var(--teal);padding-bottom:2px;white-space:nowrap;display:inline-block}
.news-text{margin-top:6px;font-size:13px;line-height:23px;color:var(--muted)}

/* newsletter */
.newsletter{left:0;top:2283px;width:1200px;height:101px;background:var(--teal)}
.newsletter-title{left:194px;top:2306px;color:var(--white);font-family:"Montserrat",sans-serif;font-weight:700;font-size:19px}
.newsletter-sub{left:194px;top:2338px;color:var(--white);font-weight:600;font-size:12px}
.newsletter-input{left:625px;top:2314px;width:271px;height:39px;background:#3fb9cc;color:#e6f6f9;font-size:13px;padding:11px 17px}
.newsletter-btn{left:896px;top:2314px;width:122px;height:39px;background:var(--white);color:var(--teal);font-family:"Montserrat",sans-serif;font-weight:700;font-size:12px;display:flex;align-items:center;justify-content:center}

/* footer */
.footer-bg{left:0;top:2384px;width:1200px;height:387px;background:linear-gradient(180deg,#245b88 0%,#1d4f7a 60%,#1a4870 100%)}
.contact-card{left:194px;top:2454px;width:257px;height:394px;background:var(--navy-card);color:var(--white);padding:0 28px}
.contact-kicker{position:absolute;left:28px;top:87px;font-size:12px;letter-spacing:2px;color:#a9c6e2}
.contact-title{position:absolute;left:28px;top:104px;font-family:"Montserrat",sans-serif;font-weight:600;font-size:22px;letter-spacing:1px;border-bottom:2px solid #7fb0dc}
.contact-row{position:absolute;left:28px;display:flex;gap:16px;align-items:center}
.contact-row .lbl{font-size:11px;color:#a9c6e2;line-height:14px}
.contact-row .val{font-size:14px;font-weight:600;line-height:18px}
.form-title{left:511px;top:2460px;color:var(--white);font-family:"Montserrat",sans-serif;font-weight:600;font-size:29px;letter-spacing:1.5px}
.field{color:var(--white);font-size:14px;font-weight:500;border-bottom:1px solid #5f86aa;height:30px;display:flex;align-items:flex-start;gap:8px}
.submit{left:513px;top:2701px;width:129px;height:39px;background:var(--lime);color:var(--white);font-family:"Montserrat",sans-serif;font-weight:700;font-size:12px;display:flex;align-items:center;justify-content:center}
.social{top:2708px;width:26px;height:26px;border-radius:50%}
.footer-nav{left:503px;top:2790px;display:flex;gap:22px;font-size:12.5px;color:var(--muted)}
.footer-nav .current{color:var(--ink);font-weight:600}
.footer-nav i{font-style:normal;color:#c2c6ca}
.copyright{left:503px;top:2838px;font-size:12px;color:var(--ink);font-weight:600}
.copyright b{color:var(--teal);font-weight:600}
</style>
</head>
<body>

<div class="abs topbar"><span>info@meridianadvisers.com</span><span>|</span><span>&#9742; 555-010-2040</span></div>
<header class="abs header"></header>
<div class="abs brand"><div class="brand-mark"></div><div class="brand-name">Meridian Advisers</div></div>
<nav class="abs nav"><span class="active">Home</span><span>About ▾</span><span>Investment</span><span>Development</span><span>Properties</span><span>Latest News</span><span>Contact</span></nav>

<div class="abs hero" role="img" aria-label="Evening view of a Mediterranean-style villa with palm trees and a green lawn"></div>

<!-- services -->
<div class="abs service" style="left:173px">
  <div class="service-icon is-active"><svg width="36" height="36" viewBox="0 0 36 36" fill="none" stroke="#fff" stroke-width="2"><path d="M4 17 18 5l14 12"/><path d="M8 14v17h20V14"/><circle cx="18" cy="22" r="5"/><path d="M18 19v6"/></svg></div>
  <div class="service-title">Property<br>Management</div>
  <div class="service-text">Lorem ipsum dolor sit amet,<br>consectetur adipisicing elit, sed<br>eiusmod tempor.</div>
</div>
<div class="abs service" style="left:390px">
  <div class="service-icon"><svg width="36" height="36" viewBox="0 0 36 36" fill="none" stroke="#fff" stroke-width="2"><path d="M6 17 18 6l12 11"/><path d="M10 14v16h16V14"/><rect x="15" y="21" width="6" height="9"/></svg></div>
  <div class="service-title">Property<br>Investment</div>
  <div class="service-text">Lorem ipsum dolor sit amet,<br>consectetur adipisicing elit, sed<br>eiusmod tempor.</div>
</div>
<div class="abs service" style="left:606px">
  <div class="service-icon"><svg width="36" height="36" viewBox="0 0 36 36" fill="none" stroke="#fff" stroke-width="2"><path d="M5 30h26"/><path d="M7 26l8-8 5 5 10-11"/><path d="M24 12h6v6"/></svg></div>
  <div class="service-title">Unlock Hidden<br>Opportunities</div>
  <div class="service-text">Lorem ipsum dolor sit amet,<br>consectetur adipisicing elit, sed<br>eiusmod tempor.</div>
</div>
<div class="abs service" style="left:823px">
  <div class="service-icon"><svg width="36" height="36" viewBox="0 0 36 36" fill="none" stroke="#fff" stroke-width="2"><path d="M4 17 16 6l12 11"/><path d="M8 14v16h16V14"/><rect x="13" y="18" width="6" height="6"/><path d="M27 22l5 5-3 3-5-5z"/></svg></div>
  <div class="service-title">Property<br>Development</div>
  <div class="service-text">Lorem ipsum dolor sit amet,<br>consectetur adipisicing elit, sed<br>eiusmod tempor.</div>
</div>

<!-- about -->
<div class="abs about-label">ABOUT</div>
<h2 class="abs heading about-title">MERIDIAN ADVISERS</h2>
<p class="abs about-text">Lorem ipsum dolor sit amet, consectetur adipisicing elit, sed do incididunt ut labore et dolore magna aliqua. Ut enim ad minim nostrudex er citation ullamco laboris nisi ut .</p>
<div class="abs about-photo" role="img" aria-label="Hands signing a contract beside a small model house"></div>

<!-- recent projects -->
<h2 class="abs heading section-title" style="top:1136px"><span>OUR RECENT PROJECTS</span></h2>

<div class="abs project-photo" style="left:0;top:1225px;width:339px;height:209px" role="img" aria-label="Two-storey house with a flowering front garden"></div>
<div class="abs project-label" style="left:0;top:1434px;width:339px;height:56px">RECENT PROJECT #1</div>

<div class="abs project-photo" style="left:348px;top:1225px;width:519px;height:281px" role="img" aria-label="Single-storey home with a landscaped patio and umbrellas"></div>
<div class="abs project-label is-featured" style="left:348px;top:1506px;width:519px;height:56px">RECENT PROJECT #2</div>

<div class="abs project-photo" style="left:877px;top:1225px;width:323px;height:281px" role="img" aria-label="Tile-roofed house with a palm tree and garage"></div>
<div class="abs project-label" style="left:877px;top:1506px;width:323px;height:56px">RECENT PROJECT #3</div>

<div class="abs project-photo" style="left:0;top:1502px;width:339px;height:348px" role="img" aria-label="Stucco house with palm trees and lawn"></div>
<div class="abs project-label" style="left:0;top:1850px;width:339px;height:58px">RECENT PROJECT #4</div>

<div class="abs project-photo" style="left:348px;top:1573px;width:362px;height:277px" role="img" aria-label="Tan two-storey house framed by a palm"></div>
<div class="abs project-label" style="left:348px;top:1850px;width:362px;height:58px">RECENT PROJECT #5</div>

<div class="abs project-photo" style="left:720px;top:1573px;width:480px;height:277px" role="img" aria-label="Mediterranean-style house with arched entry and driveway"></div>
<div class="abs project-label" style="left:720px;top:1850px;width:480px;height:58px">RECENT PROJECT #6</div>

<!-- news -->
<h2 class="abs heading section-title" style="top:2008px"><span>LATEST NEWS</span></h2>

<div class="abs news" style="left:197px">
  <div class="news-date"><svg width="16" height="14" viewBox="0 0 16 14" fill="none" stroke="#fff" stroke-width="1.4"><rect x="1" y="2" width="14" height="11"/><path d="M1 6h14M5 0v4M11 0v4"/></svg><div class="day">13</div><div class="month">July</div></div>
  <div><div class="news-title">LOREM IPSUM DOLOR</div><div class="news-text">Lorem ipsum dolor sit amet, consectetur adipisicing elit, sed eiusmod tempor.</div></div>
</div>
<div class="abs news" style="left:474px">
  <div class="news-date"><svg width="16" height="14" viewBox="0 0 16 14" fill="none" stroke="#fff" stroke-width="1.4"><rect x="1" y="2" width="14" height="11"/><path d="M1 6h14M5 0v4M11 0v4"/></svg><div class="day">11</div><div class="month">July</div></div>
  <div><div class="news-title">A DIPISICING ELIT</div><div class="news-text">Lorem ipsum dolor sit amet, consectetur adipisicing elit, sed eiusmod tempor.</div></div>
</div>
<div class="abs news" style="left:751px">
  <div class="news-date"><svg width="16" height="14" viewBox="0 0 16 14" fill="none" stroke="#fff" stroke-width="1.4"><rect x="1" y="2" width="14" height="11"/><path d="M1 6h14M5 0v4M11 0v4"/></svg><div class="day">10</div><div class="month">July</div></div>
  <div><div class="news-title">DO EIUSMOD TEMPOR</div><div class="news-text">Lorem ipsum dolor sit amet, consectetur adipisicing elit, sed eiusmod tempor.</div></div>
</div>

<!-- newsletter -->
<div class="abs newsletter"></div>
<div class="abs newsletter-title">Subscribe to our Newsletter</div>
<div class="abs newsletter-sub">Get healthy news and solutions to your problems from our experts!</div>
<div class="abs newsletter-input">Your email address..</div>
<div class="abs newsletter-btn">SUBSCRIBE ›</div>

<!-- footer -->
<div class="abs footer-bg" role="img" aria-label="Faint blue-tinted view of suburban houses"></div>

<div class="abs contact-card">
  <svg style="position:absolute;left:28px;top:34px" width="40" height="28" viewBox="0 0 40 28" fill="none" stroke="#cfe0f0" stroke-width="1.6"><circle cx="14" cy="9" r="6"/><path d="M2 27c1-7 6-10 12-10s11 3 12 10"/><circle cx="27" cy="8" r="5"/><path d="M26 16c6 0 10 3 11 10"/></svg>
  <div class="contact-kicker">GET STARTED NOW</div>
  <div class="contact-title">CONTACT INFO</div>
  <div class="contact-row" style="top:200px"><svg width="20" height="26" viewBox="0 0 20 26" fill="none" stroke="#fff" stroke-width="1.6"><path d="M10 25S2 15 2 9a8 8 0 0 1 16 0c0 6-8 16-8 16z"/><circle cx="10" cy="9" r="3"/></svg><div><div class="lbl">Address:</div><div class="val">48 Harbor Lane<br>Eastfield, SC 29000</div></div></div>
  <div class="contact-row" style="top:276px"><svg width="22" height="22" viewBox="0 0 22 22" fill="none" stroke="#fff" stroke-width="1.6"><path d="M3 2h5l2 5-3 2c1 3 3 5 6 6l2-3 5 2v5c0 1-1 2-2 2C9 21 1 13 1 4c0-1 1-2 2-2z"/></svg><div><div class="lbl">Phone:</div><div class="val">555 010 2040</div></div></div>
  <div class="contact-row" style="top:348px"><svg width="22" height="16" viewBox="0 0 22 16" fill="none" stroke="#fff" stroke-width="1.6"><rect x="1" y="1" width="20" height="14"/><path d="M1 1l10 8 10-8"/></svg><div><div class="lbl">Email:</div><div class="val" style="font-size:13px">info@meridianadvisers.com</div></div></div>
</div>

<h2 class="abs form-title">REQUEST AN INFORMATION</h2>
<div class="abs field" style="left:511px;top:2522px;width:244px">&#9786; First Name</div>
<div class="abs field" style="left:768px;top:2522px;width:242px">&#9786; Last Name</div>
<div class="abs field" style="left:511px;top:2580px;width:244px">&#9742; Phone</div>
<div class="abs field" style="left:768px;top:2580px;width:242px">&#9993; Email</div>
<div class="abs field" style="left:511px;top:2632px;width:499px;height:44px">&#9993; Message</div>
<div class="abs submit">SUBMIT ›</div>
<div class="abs social" style="left:894px;background:#3b5bb5"></div>
<div class="abs social" style="left:935px;background:#2b9ee8"></div>
<div class="abs social" style="left:978px;background:#e0413b"></div>

<nav class="abs footer-nav"><span class="current">Home</span><i>•</i><span>About</span><i>•</i><span>Investment</span><i>•</i><span>Development</span><i>•</i><span>Properties</span><i>•</i><span>Contact</span></nav>
<div class="abs copyright">© 2017 <b>Meridian Advisers MultiFamily Properties.</b> All rights reserved</div>

</body>
</html>
```